Daxholm APP redesign and color change

I am looking for a new design for my app. Please see the attached current design.

Currently, I have a functioning app but the colors and design are awful!
The logo is great but the rest of the app needs a refresh.
(Logo hi res not yet available but will upload soon.)
New colors or anything that is cutting edge.

Basically: It is a secure social media app within a school system where the teachers, students and parents can text, exchange photos, plan curriculum, etc.

I NEED ONLY landing page with a new look!
Looking for one distinct design for the landing page with new look.
The developer will apply this one design towards the rest of the pages/app screens.

Because part of the social media I need the feel and look of what is now the trend. Something that will attract and keep the client(s) interested. I am really leaving all the creative work to the designer and open to any suggestions.
Updates

Target Market(s)

Schools, community, teachers, students, colleges, sport teams

Industry/Entity Type

Non Profit

Font styles to use
Serif
Sans Serif

Colors

Designer to choose colors to be used in the design.

Requirements
Must have
• Sharp, trendy, millennial feel
Nice to have
• Up to designer
Should not have
• Up to designer

```html
<!DOCTYPE html>
<html lang="en">
<head>
<meta charset="UTF-8">
<title>Daxholm – Landing</title>
<link rel="stylesheet" href="https://fonts.googleapis.com/css2?family=Roboto:wght@400;500;700&display=swap">
<style>
  :root {
    --bg: #ecebef;
    --ink: #1f2a4d;
    --ink-soft: #4a5270;
    --white: #ffffff;
    --teal: #1fb7b3;
    --teal-mid: #25a9c6;
    --teal-deep: #1d7fa8;
    --pink: #e8508c;
    --pink-soft: #f48bb4;
    --pink-deep: #d63a78;
    --orange: #f2b23e;
    --orange-soft: #f7cf7a;
    --orange-deep: #e2813a;
    --purple: #a957d6;
    --purple-soft: #c98ae6;
    --purple-deep: #6f37bd;
    --blue: #2160c4;
    --ring: #d9d9de;
  }
  * { box-sizing: border-box; margin: 0; padding: 0; }
  html, body {
    width: 1200px;
    height: 800px;
    overflow: hidden;
    background: var(--bg);
    font-family: "Roboto", Arial, sans-serif;
  }
  .canvas {
    width: 1200px;
    height: 800px;
    display: flex;
    align-items: center;
    justify-content: center;
  }
  .screen {
    position: relative;
    width: 400px;
    height: 710px;
    background: var(--white);
    display: flex;
    flex-direction: column;
    overflow: hidden;
    box-shadow: 0 10px 40px rgba(31, 42, 77, 0.15);
  }
  .hero {
    position: relative;
    height: 470px;
    display: grid;
    grid-template-columns: 1fr 1fr;
    grid-template-rows: 1fr 1fr;
  }
  .hero-tile { display: block; }
  .tile-teacher {
    background:
      radial-gradient(ellipse 70% 60% at 62% 30%, rgba(255,255,255,0.28), transparent 70%),
      radial-gradient(ellipse 80% 60% at 20% 85%, rgba(20,90,140,0.35), transparent 70%),
      linear-gradient(160deg, var(--teal) 0%, var(--teal-mid) 55%, var(--teal-deep) 100%);
  }
  .tile-phone {
    background:
      radial-gradient(ellipse 70% 55% at 40% 35%, rgba(255,255,255,0.3), transparent 70%),
      radial-gradient(ellipse 70% 60% at 85% 90%, rgba(160,30,90,0.3), transparent 70%),
      linear-gradient(160deg, var(--pink-soft) 0%, var(--pink) 55%, var(--pink-deep) 100%);
  }
  .tile-reader {
    background:
      radial-gradient(ellipse 60% 70% at 60% 45%, rgba(255,255,255,0.3), transparent 70%),
      radial-gradient(ellipse 70% 50% at 15% 95%, rgba(190,90,30,0.35), transparent 70%),
      linear-gradient(165deg, var(--orange-soft) 0%, var(--orange) 45%, var(--orange-deep) 100%);
  }
  .tile-student {
    background:
      radial-gradient(ellipse 55% 65% at 50% 40%, rgba(255,255,255,0.3), transparent 70%),
      radial-gradient(ellipse 70% 55% at 90% 95%, rgba(60,20,130,0.35), transparent 70%),
      linear-gradient(160deg, var(--purple-soft) 0%, var(--purple) 50%, var(--purple-deep) 100%);
  }
  .brand-badge {
    position: absolute;
    left: 50%;
    top: 50%;
    width: 100px;
    height: 100px;
    transform: translate(-50%, -50%);
    border-radius: 50%;
    background: var(--white);
    border: 4px solid var(--ring);
    display: flex;
    align-items: center;
    justify-content: center;
    box-shadow: 0 3px 10px rgba(0, 0, 0, 0.18);
  }
  .brand-name {
    font-size: 15px;
    font-weight: 500;
    color: var(--ink);
  }
  .welcome {
    flex: 1;
    display: flex;
    flex-direction: column;
    align-items: center;
    padding-top: 28px;
    text-align: center;
  }
  .welcome-title {
    font-size: 22px;
    font-weight: 500;
    color: var(--ink);
    margin-bottom: 8px;
  }
  .welcome-text {
    font-size: 13px;
    line-height: 1.45;
    color: var(--ink-soft);
    width: 240px;
  }
  .actions {
    display: flex;
    gap: 12px;
    margin-top: 30px;
  }
  .btn {
    width: 132px;
    height: 42px;
    border-radius: 21px;
    display: flex;
    align-items: center;
    justify-content: center;
    color: var(--white);
    font-size: 15px;
    font-weight: 500;
    text-decoration: none;
  }
  .btn-login  { background: linear-gradient(90deg, var(--pink-soft), var(--pink)); }
  .btn-signup { background: linear-gradient(90deg, var(--teal), var(--blue)); }
</style>
</head>
<body>
  <main class="canvas">
    <section class="screen">
      <div class="hero">
        <div class="hero-tile tile-teacher" role="img" aria-label="Photo of a smiling teacher in a classroom, teal tint"></div>
        <div class="hero-tile tile-phone" role="img" aria-label="Photo of hands holding phones, pink tint"></div>
        <div class="hero-tile tile-reader" role="img" aria-label="Photo of a man reading on a tablet, orange tint"></div>
        <div class="hero-tile tile-student" role="img" aria-label="Photo of a smiling student holding books, purple tint"></div>
        <div class="brand-badge"><span class="brand-name">Daxholm</span></div>
      </div>
      <div class="welcome">
        <h1 class="welcome-title">Join Today</h1>
        <p class="welcome-text">Interact with your Teachers students and Parents in better way</p>
        <div class="actions">
          <a class="btn btn-login" href="#">Login</a>
          <a class="btn btn-signup" href="#">Sign up</a>
        </div>
      </div>
    </section>
  </main>
</body>
</html>
```